Business cards for Norwegian software consultancy business

We are in need of business cards for our Norwegian consultancy company.
“Talvik Brensor AS” specializes in software development, architecture and agile methodology, providing mostly on-site services at customers.
The cards should reflect a certain level of business professionalism with an elegant touch, while paying tribute to our modern and technological heritage. Our logo should be featured, as well as room for basic information about the cardholder and legal information of the company (company name, address and VAT number).
We would like our cards to reflect that we are a modern consulting company. It should present a professional image that people will remember. The texture and color pallette should reflect our professionalism and reliability, so we prefer a light color pallette with colors such as gray, white, blue and black. The number of colors used should however not be overwhelming, with the text being distinct and readable.
We are open to untraditional layouts and playful designs as long as they communicate the intent stated above.
You could also take a look at our website http://www.brensor.no for input on our visual profile.
Our logo is attached in the form of vectors and rasterized PNG. Please comment if you would like the black-white and/or inverted versions as well.
Architecture
Company information:
Talvik Brensor AS
Lindeholtveien 7, 3142 Vestskogen
461 82 915
info@brensor.no
www.brensor.no
Employee information:
Full name
Title
Email
Phone

```html
<!DOCTYPE html>
<html lang="no">
<head>
<meta charset="utf-8">
<title>Talvik Brensor AS – Business Card</title>
<link rel="stylesheet" href="https://fonts.googleapis.com/css2?family=Questrial&display=swap">
<style>
  :root {
    --page-bg: #e9ebee;
    --card-white: #ffffff;
    --ink: #2b2b2b;
    --ink-soft: #3a3a3a;
    --icon-blue: #5d8fd3;
    --blue-light: #9fd3f2;
    --blue-sky: #5fb6e8;
    --blue-mid: #3f8fd6;
    --blue-deep: #3474c4;
    --blue-steel: #7ea6d8;
    --blue-cyan: #2bb6ea;
  }
  * { box-sizing: border-box; margin: 0; padding: 0; }
  html, body {
    width: 1200px;
    height: 1200px;
    overflow: hidden;
    background: var(--page-bg);
    font-family: "Questrial", sans-serif;
  }
  .card {
    position: absolute;
    left: 75px;
    top: 290px;
    width: 1050px;
    height: 620px;
    background: var(--card-white);
    display: flex;
    box-shadow: 0 10px 30px rgba(0, 0, 0, 0.18);
  }
  .card-art {
    position: relative;
    width: 630px;
    height: 100%;
    overflow: hidden;
  }
  .art-fill {
    position: absolute;
    inset: 0;
    background:
      linear-gradient(200deg, var(--blue-steel) 0%, transparent 45%),
      linear-gradient(160deg, var(--blue-light) 0%, var(--blue-mid) 35%, var(--blue-sky) 60%, var(--blue-deep) 85%, var(--blue-cyan) 100%);
  }
  .brand-band {
    position: absolute;
    left: 0;
    top: 232px;
    width: 478px;
    height: 104px;
    background: var(--card-white);
    display: flex;
    align-items: center;
    padding-left: 118px;
    gap: 16px;
  }
  .brand-mark {
    width: 22px;
    height: 22px;
    background: var(--ink);
    flex: none;
  }
  .brand-name {
    font-size: 34px;
    letter-spacing: 2px;
    color: var(--ink);
    white-space: nowrap;
  }
  .band-bar {
    position: absolute;
    top: 232px;
    height: 104px;
    width: 8px;
    background: var(--card-white);
  }
  .band-bar.first { left: 490px; }
  .band-bar.second { left: 506px; }
  .card-info {
    flex: 1;
    display: flex;
    flex-direction: column;
    align-items: center;
    justify-content: center;
    gap: 30px;
    color: var(--ink-soft);
    text-align: center;
  }
  .info-item {
    display: flex;
    flex-direction: column;
    align-items: center;
    gap: 14px;
    font-size: 21px;
    line-height: 1.35;
  }
  .info-icon { width: 32px; height: 32px; fill: var(--icon-blue); }
  .info-icon.stroke { fill: none; stroke: var(--icon-blue); stroke-width: 2; }
</style>
</head>
<body>
  <main class="card">
    <section class="card-art">
      <div class="art-fill" role="img" aria-label="Overlapping blue geometric facets in light, sky and deep blue tones"></div>
      <div class="brand-band">
        <span class="brand-mark"></span>
        <span class="brand-name">TALVIK BRENSOR</span>
      </div>
      <span class="band-bar first"></span>
      <span class="band-bar second"></span>
    </section>

    <section class="card-info">
      <div class="info-item address">
        <svg class="info-icon" viewBox="0 0 24 24" aria-hidden="true"><path d="M12 2a7 7 0 0 0-7 7c0 5 7 13 7 13s7-8 7-13a7 7 0 0 0-7-7zm0 9.5A2.5 2.5 0 1 1 12 6.5a2.5 2.5 0 0 1 0 5z"/></svg>
        <p>Lindeholtveien 7<br>3142 Vestskogen</p>
      </div>
      <div class="info-item phone">
        <svg class="info-icon" viewBox="0 0 24 24" aria-hidden="true"><path d="M6.6 10.8a15.1 15.1 0 0 0 6.6 6.6l2.2-2.2a1 1 0 0 1 1-.25 11.4 11.4 0 0 0 3.6.57 1 1 0 0 1 1 1V20a1 1 0 0 1-1 1A17 17 0 0 1 3 4a1 1 0 0 1 1-1h3.5a1 1 0 0 1 1 1c0 1.25.2 2.45.57 3.57a1 1 0 0 1-.25 1z"/></svg>
        <p>461 82 915</p>
      </div>
      <div class="info-item email">
        <svg class="info-icon" viewBox="0 0 24 24" aria-hidden="true"><path d="M2 5h20v14H2z M2 5l10 8 10-8" fill="var(--icon-blue)" stroke="#fff" stroke-width="1.2"/></svg>
        <p>info@brensor.no</p>
      </div>
      <div class="info-item web">
        <svg class="info-icon stroke" viewBox="0 0 24 24" aria-hidden="true"><circle cx="12" cy="12" r="9.5"/><ellipse cx="12" cy="12" rx="4" ry="9.5"/><path d="M2.5 12h19M4 7h16M4 17h16"/></svg>
        <p>www.brensor.no</p>
      </div>
    </section>
  </main>
</body>
</html>
```